DEAN COLLOPY PROPERTY SERVICES

I want a business card that is clean and simple.
'Dean Collopy Property Services' is the title.
Somewhere on the card needs to be 'Carpentry, Tiling, painting and garden services'

On the back of card
PH 087 394 1526
email: deancollopypropertyservices@fernmail.net

I have attached a picture of my other business. I would like the font and design to be similar to the bathroom business.

Many thanks.

```html
<!DOCTYPE html>
<html lang="en">
<head>
<meta charset="utf-8">
<title>Dean Collopy Property Services – Business Card</title>
<link rel="stylesheet" href="https://fonts.googleapis.com/css2?family=Montserrat:wght@400;700&family=Nunito+Sans:wght@400&display=swap">
<style>
  :root {
    --stage-light: #ededed;
    --stage-dark: #8a8a8a;
    --card-white: #ffffff;
    --card-black: #000000;
    --ink: #111111;
    --ink-muted: #7a7a7a;
    --ink-icon: #555555;
    --paper-text: #ffffff;
  }
  * { margin: 0; padding: 0; box-sizing: border-box; }
  html, body { width: 1200px; height: 1200px; overflow: hidden; }
  body {
    background: radial-gradient(ellipse at 50% 40%, var(--stage-light) 0%, #cfcfcf 45%, var(--stage-dark) 100%);
    font-family: "Nunito Sans", Arial, sans-serif;
    position: relative;
  }
  .card {
    position: absolute;
    left: 160px;
    width: 880px;
    height: 500px;
    box-shadow: 0 8px 24px rgba(0,0,0,0.25);
  }
  .card--front { top: 70px; background: var(--card-white); color: var(--ink); }
  .card--back { top: 630px; background: var(--card-black); color: var(--paper-text); }

  .wordmark { font-family: "Montserrat", Arial, sans-serif; font-weight: 400; text-align: center; }
  .wordmark__name { display: block; line-height: 1; }
  .wordmark__line { display: block; text-transform: uppercase; }

  .card--front .wordmark { position: absolute; right: 58px; top: 88px; color: var(--ink); }
  .card--front .wordmark__name { font-size: 50px; letter-spacing: 0.5px; }
  .card--front .wordmark__line { font-size: 13px; letter-spacing: 6px; margin-top: 6px; }

  .holder { position: absolute; left: 60px; top: 258px; }
  .holder__name { font-family: "Montserrat", Arial, sans-serif; font-weight: 700; font-size: 38px; line-height: 1.1; }
  .holder__role { font-size: 24px; color: var(--ink-muted); margin-top: 6px; }

  .contact { position: absolute; left: 60px; top: 392px; list-style: none; font-size: 25px; color: var(--ink); }
  .contact__item { display: flex; align-items: center; gap: 12px; line-height: 36px; }
  .contact__icon { width: 20px; height: 20px; fill: var(--ink-icon); flex: none; }

  .card--back .wordmark { position: absolute; left: 0; right: 0; top: 180px; color: var(--paper-text); }
  .card--back .wordmark__name { font-size: 78px; letter-spacing: 1px; }
  .card--back .wordmark__line { font-size: 19px; letter-spacing: 9px; margin-top: 10px; }

  .services { position: absolute; left: 0; right: 0; top: 410px; text-align: center; font-size: 26px; color: var(--paper-text); }
</style>
</head>
<body>
  <section class="card card--front" aria-label="Business card front">
    <div class="wordmark">
      <span class="wordmark__name">Dean Collopy</span>
      <span class="wordmark__line">Property Services</span>
    </div>
    <div class="holder">
      <p class="holder__name">Dean Collopy</p>
      <p class="holder__role">Owner</p>
    </div>
    <ul class="contact">
      <li class="contact__item">
        <svg class="contact__icon" viewBox="0 0 24 24" aria-hidden="true"><path d="M6.6 10.8a15.1 15.1 0 0 0 6.6 6.6l2.2-2.2a1 1 0 0 1 1-.25 11.4 11.4 0 0 0 3.6.57 1 1 0 0 1 1 1V20a1 1 0 0 1-1 1A17 17 0 0 1 3 4a1 1 0 0 1 1-1h3.5a1 1 0 0 1 1 1c0 1.25.2 2.45.57 3.57a1 1 0 0 1-.25 1z"/></svg>
        <span>087 394 1526</span>
      </li>
      <li class="contact__item">
        <svg class="contact__icon" viewBox="0 0 24 24" aria-hidden="true"><path d="M2 5h20v14H2z M3.5 6.5 12 13l8.5-6.5" fill="var(--ink-icon)" stroke="#ffffff" stroke-width="1.3"/></svg>
        <span>deancollopypropertyservices@fernmail.net</span>
      </li>
    </ul>
  </section>

  <section class="card card--back" aria-label="Business card back">
    <div class="wordmark">
      <span class="wordmark__name">Dean Collopy</span>
      <span class="wordmark__line">Property Services</span>
    </div>
    <p class="services">Carpentry, Tiling, Painting and Garden Services</p>
  </section>
</body>
</html>
```